Sports massage flyer

I need an advert designed that can be used in a magazine, as a poster/flyer and on facebook. This is to advertise Sports massage.

I have attached a picture and my logo. I'm looking for something clean and simple.
I will need this in various file types suitable for print, facebook, email etc

It needs to have the following information on the leaflet:

Mobile sports massage therapist (headline)

• Maintenance massage
• Pre and post event massage
• Flexible home or work appointments
• Evening and weekend appointments available

For more information please contact me:
Email dan@corvelmail.example
Mob: 071504938215

```html
<!DOCTYPE html>
<html lang="en">
<head>
<meta charset="utf-8">
<title>Corvel Motion – Mobile Sports Massage Therapist</title>
<link href="https://fonts.googleapis.com/css2?family=Montserrat:wght@400;500;600;700&display=swap" rel="stylesheet">
<style>
  :root {
    --page-bg: #e9e8ec;
    --navy: #2e3c56;
    --navy-deep: #263248;
    --navy-soft: #34435f;
    --navy-band: #233047;
    --white: #ffffff;
    --photo-light: #dfe4ea;
    --photo-mid: #b9c2cd;
    --photo-dark: #3a4150;
  }
  html, body {
    margin: 0;
    padding: 0;
    width: 1040px;
    height: 1200px;
    overflow: hidden;
    background: var(--page-bg);
  }
  .canvas {
    position: relative;
    width: 1040px;
    height: 1200px;
  }
  .flyer {
    position: absolute;
    left: 79px;
    top: 31px;
    width: 882px;
    height: 1138px;
    display: block;
    font-family: "Montserrat", sans-serif;
  }
  .navy-field { fill: var(--navy); }
  .wave-back { fill: var(--navy-deep); }
  .arch-panel { fill: var(--navy-soft); }
  .contact-band { fill: var(--navy-band); }
  .ribbon { fill: var(--navy-band); }
  .lens { fill: var(--white); fill-opacity: 0.32; }
  .brand-name { fill: var(--navy-band); font-size: 20px; font-weight: 600; letter-spacing: 0.5px; }
  .headline { fill: var(--white); font-size: 24px; font-weight: 700; letter-spacing: 0.6px; }
  .ribbon-title { fill: var(--white); font-size: 22px; font-weight: 700; letter-spacing: 1px; }
  .service-item { fill: var(--white); font-size: 17px; font-weight: 500; }
  .contact-lead { fill: var(--white); font-size: 13.5px; font-weight: 700; }
  .contact-detail { fill: var(--white); font-size: 12.5px; font-weight: 500; }
  .contact-icon { fill: none; stroke: var(--white); stroke-width: 1.1; stroke-linejoin: round; stroke-linecap: round; }
</style>
</head>
<body>
<div class="canvas">
  <svg class="flyer" viewBox="0 0 580 748" xmlns="http://www.w3.org/2000/svg">
    <defs>
      <linearGradient id="photoTone" x1="0" y1="0" x2="1" y2="1">
        <stop offset="0" stop-color="var(--photo-dark)"/>
        <stop offset="0.45" stop-color="var(--photo-mid)"/>
        <stop offset="1" stop-color="var(--photo-light)"/>
      </linearGradient>
      <filter id="headlineGlow" x="-10%" y="-50%" width="120%" height="200%">
        <feGaussianBlur in="SourceAlpha" stdDeviation="3" result="blur"/>
        <feFlood flood-color="#ffffff" flood-opacity="0.55"/>
        <feComposite in2="blur" operator="in" result="glow"/>
        <feMerge><feMergeNode in="glow"/><feMergeNode in="SourceGraphic"/></feMerge>
      </filter>
      <path id="headlineArc" d="M22,316 Q290,482 558,303"/>
    </defs>

    <rect class="hero-photo" x="0" y="0" width="580" height="420" fill="url(#photoTone)" role="img" aria-label="Photo of a therapist giving a sports massage to a client's raised leg"/>

    <circle class="lens" cx="290" cy="248" r="205"/>

    <text class="brand-name" x="290" y="272" text-anchor="middle">Corvel Motion</text>

    <path class="navy-field" d="M0,205 Q290,545 580,178 L580,748 L0,748 Z"/>
    <path class="wave-back" d="M0,432 C110,398 210,402 290,422 C370,402 470,398 580,432 L580,748 L0,748 Z"/>
    <path class="arch-panel" d="M30,748 L30,560 C30,430 550,430 550,560 L550,748 Z"/>
    <path class="navy-field" d="M0,470 C120,440 460,440 580,470 L580,748 L0,748 Z" opacity="0.55"/>

    <text class="headline" filter="url(#headlineGlow)">
      <textPath href="#headlineArc" startOffset="50%" text-anchor="middle">MOBILE SPORTS MASSAGE THERAPIST</textPath>
    </text>

    <polygon class="ribbon" points="175,446 410,446 399,473 410,500 175,500 186,473"/>
    <text class="ribbon-title" x="292.5" y="481" text-anchor="middle">OUR&#160; SERVICE</text>

    <g class="service-list" text-anchor="middle">
      <text class="service-item" x="290" y="526">Maintenance massage</text>
      <text class="service-item" x="290" y="562">Pre and post event massage</text>
      <text class="service-item" x="290" y="597">Flexible home or work appointments</text>
      <text class="service-item" x="290" y="633">Evening and weekend appointments available</text>
    </g>

    <rect class="contact-band" x="0" y="663" width="580" height="85"/>
    <text class="contact-lead" x="290" y="700" text-anchor="middle">For more information please contact me:</text>

    <g class="contact-email">
      <rect class="contact-icon" x="112" y="711" width="13" height="9" rx="1"/>
      <path class="contact-icon" d="M112,712 L118.5,717 L125,712"/>
      <text class="contact-detail" x="131" y="720">dan@corvelmail.example</text>
    </g>
    <g class="contact-phone">
      <path class="contact-icon" d="M320,710 l3,-1 l2,4 l-2,1.5 a8,8 0 0 0 4,4 l1.5,-2 l4,2 l-1,3 c-6,1 -12,-5 -11.5,-11.5 z"/>
      <text class="contact-detail" x="340" y="720">071504938215</text>
    </g>
  </svg>
</div>
</body>
</html>
```